Real Estate Agent needs business card design

We have logo designed already, want to have business card designed. Very interested in those smaller size business card as they look very trendy. Business name is called TOVANE REALTY

Industry/Entity Type

Business

```html
<!DOCTYPE html>
<html lang="en">
<head>
<meta charset="utf-8">
<title>Tovane Realty – Business Card</title>
<link rel="stylesheet" href="https://fonts.googleapis.com/css2?family=Playfair+Display:wght@700&family=Open+Sans:wght@400&display=swap">
<style>
  :root {
    --backdrop: #111111;
    --card-white: #ffffff;
    --card-gold: #cfa56f;
    --brand-gold: #c9a06a;
    --ink: #1c1c1c;
    --ink-soft: #2a2a2a;
  }
  * { box-sizing: border-box; margin: 0; padding: 0; }
  html, body {
    width: 1200px;
    height: 1000px;
    overflow: hidden;
    background: var(--backdrop);
  }
  .canvas {
    position: relative;
    width: 1200px;
    height: 1000px;
  }
  .card {
    position: absolute;
    top: 360px;
    width: 500px;
    height: 280px;
    box-shadow: 0 6px 18px rgba(0,0,0,0.5);
  }
  .card--front {
    left: 70px;
    background: var(--card-white);
    display: flex;
    align-items: center;
    justify-content: center;
  }
  .brand {
    display: flex;
    align-items: center;
    gap: 14px;
  }
  .brand__mark {
    width: 18px;
    height: 18px;
    background: var(--brand-gold);
  }
  .brand__name {
    font-family: "Playfair Display", Georgia, serif;
    font-weight: 700;
    font-size: 34px;
    letter-spacing: 2px;
    color: var(--ink);
  }
  .card--back {
    left: 630px;
    background: var(--card-gold);
    padding: 52px 44px 0 40px;
    text-align: right;
    color: var(--ink);
  }
  .agent__name {
    font-family: "Playfair Display", Georgia, serif;
    font-weight: 700;
    font-size: 30px;
    line-height: 1.1;
  }
  .agent__role {
    font-family: "Open Sans", Arial, sans-serif;
    font-size: 15px;
    color: var(--ink-soft);
    margin-top: 2px;
  }
  .contact {
    list-style: none;
    margin-top: 24px;
    font-family: "Open Sans", Arial, sans-serif;
    font-size: 16px;
    line-height: 1.6;
    color: var(--ink-soft);
  }
</style>
</head>
<body>
  <main class="canvas">
    <section class="card card--front" aria-label="Card front">
      <div class="brand">
        <span class="brand__mark" aria-hidden="true"></span>
        <span class="brand__name">TOVANE REALTY</span>
      </div>
    </section>

    <section class="card card--back" aria-label="Card back">
      <h1 class="agent__name">Helena Marsh</h1>
      <p class="agent__role">Senior Property Consultant</p>
      <ul class="contact">
        <li>0491 570 156</li>
        <li>www.tovanerealty.com.au</li>
        <li>7C, 48 Harbour Road, Northgate, NSW 2099</li>
      </ul>
    </section>
  </main>
</body>
</html>
```